Rooted Ready Rising: Quiet Roots, Open Doors, Steady Hands

I want a modern and clean looking book cover. 5.25x8

Title
Rooted Ready Rising

Subtitle
Quiet Roots, Open Doors, Steady Hands

I don’t just want a graphic, I want it to make sense. If it can just be the words and a textured looking background, I’ll be ok with that too. I just want it to look crisp, clean, modern.

I want the back to have my book blurb and bio attached with the pic that’s attached.

Target Market(s)

Self help

Requirements
Must have
• Modern, clean look, look professional, attract customers.

```html
<!DOCTYPE html>
<html lang="en">
<head>
<meta charset="utf-8">
<title>Rooted Ready Rising – Book Cover</title>
<link rel="stylesheet" href="https://fonts.googleapis.com/css2?family=Bebas+Neue&family=League+Spartan:wght@700;800&display=swap">
<style>
  :root {
    --backdrop: #e3e3e3;
    --cover-white: #ffffff;
    --cover-fade: #f4f4f5;
    --ink-navy: #0e1638;
    --navy-soft: #5a6386;
    --summit-orange: #e65106;
    --orange-soft: #f39a5c;
  }
  html, body {
    margin: 0;
    padding: 0;
    width: 1027px;
    height: 1200px;
    overflow: hidden;
    background: var(--backdrop);
  }
  .book-cover {
    position: absolute;
    left: 118px;
    top: 20px;
    width: 791px;
    height: 1160px;
    display: block;
  }
  .title-line {
    font-family: "League Spartan", "Arial Black", sans-serif;
    font-weight: 800;
    font-size: 300px;
    fill: var(--ink-navy);
  }
  .subtitle-line {
    font-family: "League Spartan", "Arial", sans-serif;
    font-weight: 700;
    font-size: 62px;
    fill: var(--ink-navy);
  }
  .author-name {
    font-family: "Bebas Neue", "Arial Narrow", sans-serif;
    font-size: 54px;
    letter-spacing: 1px;
    fill: var(--ink-navy);
  }
</style>
</head>
<body>
  <svg class="book-cover" viewBox="0 0 983 1442" xmlns="http://www.w3.org/2000/svg" aria-label="Rooted Ready Rising book cover">
    <defs>
      <linearGradient id="cover-surface" x1="0" y1="0" x2="0" y2="1">
        <stop offset="0" stop-color="var(--cover-white)"/>
        <stop offset="1" stop-color="var(--cover-fade)"/>
      </linearGradient>
      <linearGradient id="summit-tone" x1="0" y1="0" x2="1" y2="1">
        <stop offset="0" stop-color="var(--orange-soft)"/>
        <stop offset="1" stop-color="var(--summit-orange)"/>
      </linearGradient>
      <linearGradient id="figure-tone" x1="0" y1="0" x2="0" y2="1">
        <stop offset="0" stop-color="var(--navy-soft)" stop-opacity="0.35"/>
        <stop offset="1" stop-color="var(--ink-navy)" stop-opacity="0.55"/>
      </linearGradient>
    </defs>

    <rect class="cover-base" x="0" y="0" width="983" height="1442" fill="url(#cover-surface)"/>

    <rect class="summit-area" x="300" y="975" width="683" height="467" fill="url(#summit-tone)"
          role="img" aria-label="Illustration of an orange mountain rising from the lower left to a peak on the right"/>

    <rect class="figure-area figure-area--standing" x="100" y="385" width="120" height="272" fill="url(#figure-tone)"
          role="img" aria-label="Illustration of a man standing with hands in pockets"/>
    <rect class="figure-area figure-area--summit" x="745" y="705" width="150" height="265" fill="url(#summit-tone)"
          role="img" aria-label="Illustration of a person on the summit raising a fist in triumph"/>

    <g class="cover-title">
      <text class="title-line" x="140" y="315" textLength="718" lengthAdjust="spacingAndGlyphs">ROOTED</text>
      <text class="title-line" x="275" y="629" textLength="587" lengthAdjust="spacingAndGlyphs">READY</text>
      <text class="title-line" x="140" y="937" textLength="550" lengthAdjust="spacingAndGlyphs">RISING</text>
    </g>

    <g class="cover-subtitle">
      <text class="subtitle-line" x="140" y="1042" textLength="718" lengthAdjust="spacing">QUIET ROOTS</text>
      <text class="subtitle-line" x="140" y="1147" textLength="718" lengthAdjust="spacing">OPEN DOORS</text>
      <text class="subtitle-line" x="140" y="1242" textLength="718" lengthAdjust="spacing">STEADY HANDS</text>
    </g>

    <text class="author-name" x="490" y="1389" text-anchor="middle">MARISA HOLLOWAY</text>
  </svg>
</body>
</html>
```